Trailer wrap

Looking for a trailer wrap. I have attached a file of my logo. Also use the phone number 555-304-2617. integrate one or both of the following slogans - ""Solutions You Can Trust" - ""Prompt. Able. Careful. Honest. That’s the PACH Difference" If possible integrate a United States flag, possibly in grayscale. The following are my colors: Orange F16A21 Blue 4D91D9.

```html
<!DOCTYPE html>
<html lang="en">
<head>
<meta charset="utf-8">
<title>PACH HVAC &amp; Plumbing – Trailer Wrap</title>
<link rel="stylesheet" href="https://fonts.googleapis.com/css2?family=Anton&family=Caveat:wght@600&display=swap">
<style>
  :root{
    --stage:#2f2f2f;
    --ink:#000000;
    --orange:#f16a21;
    --blue:#4d91d9;
    --white:#ffffff;
    --flag-light:#cfcfcf;
    --flag-dark:#3a3a3a;
  }
  *{box-sizing:border-box;margin:0;padding:0}
  html,body{width:1200px;height:849px;overflow:hidden;background:var(--stage)}
  .canvas{position:relative;width:1200px;height:849px}
  .panel{position:absolute;background:var(--ink);overflow:hidden}
  .panel-side{left:40px;top:262px;width:700px;height:325px}
  .panel-rear{left:790px;top:244px;width:360px;height:360px}
  .layer{position:absolute;inset:0}
  .flag{position:absolute;background:linear-gradient(160deg,var(--flag-light),var(--flag-dark) 45%,var(--flag-light) 70%,var(--flag-dark));opacity:.3}
  .headline{position:absolute;left:27px;top:12px;font-family:"Anton",sans-serif;color:var(--blue);font-size:44px;line-height:45px;letter-spacing:-.5px;text-transform:uppercase}
  .signoff{position:absolute;left:30px;top:198px;width:190px;text-align:center;font-family:"Caveat",cursive;color:var(--blue);font-size:24px;line-height:22px}
  .phone{position:absolute;display:flex;align-items:center;gap:8px;font-family:"Anton",sans-serif;color:var(--white);white-space:nowrap}
  .panel-side .phone{left:30px;top:274px;font-size:32px;line-height:40px}
  .panel-rear .phone{left:150px;top:292px;font-size:26px;line-height:34px}
  .phone svg{display:block}
  .services{position:absolute;right:22px;top:12px;font-family:"Anton",sans-serif;color:var(--white);font-size:21px;line-height:31px;text-align:right;text-transform:uppercase}
  .services li{list-style:none;display:flex;justify-content:flex-end;align-items:center;gap:8px}
  .promise{position:absolute;right:18px;top:152px;font-family:"Anton",sans-serif;color:var(--orange);font-size:35px;line-height:38px;text-align:right;text-transform:uppercase}
  .brand{position:absolute;text-align:center;font-family:"Anton",sans-serif;color:var(--orange);text-transform:uppercase}
  .panel-side .brand{left:270px;top:100px;width:200px;font-size:46px;line-height:60px}
  .panel-rear .brand{left:92px;top:128px;width:200px;font-size:42px;line-height:56px}
</style>
</head>
<body>
<main class="canvas">

  <section class="panel panel-side" aria-label="Trailer side panel">
    <svg class="layer" width="700" height="325" viewBox="0 0 700 325">
      <path d="M470 0H700V175Q640 140 560 150L500 90Z" fill="var(--orange)"/>
      <rect x="15" y="250" width="210" height="75" fill="var(--blue)" opacity=".35"/>
      <circle cx="363" cy="139" r="140" fill="none" stroke="var(--blue)" stroke-width="26" stroke-dasharray="420 460" transform="rotate(110 363 139)"/>
      <circle cx="363" cy="139" r="128" fill="var(--orange)"/>
      <circle cx="370" cy="132" r="120" fill="var(--ink)"/>
    </svg>
    <div class="flag" style="left:0;top:0;width:330px;height:95px" role="img" aria-label="Grayscale waving United States flag"></div>
    <div class="flag" style="left:580px;top:200px;width:120px;height:125px" role="img" aria-label="Grayscale waving United States flag"></div>

    <h1 class="headline">Prompt.<br>Able.<br>Careful.<br>Honest.</h1>
    <p class="signoff">That’s the PACH<br>difference</p>
    <p class="phone">
      <svg width="22" height="22" viewBox="0 0 24 24" aria-hidden="true"><circle cx="12" cy="12" r="12" fill="var(--white)"/><path d="M8 6l2 3-1.5 1.5a8 8 0 0 0 5 5L15 14l3 2-1 2.5C11 18 6 13 5.5 7Z" fill="var(--ink)"/></svg>
      555-304-2617
    </p>

    <p class="brand">PACH</p>

    <ul class="services">
      <li>Cooling <svg width="18" height="18" viewBox="0 0 20 20" aria-hidden="true"><path d="M10 1V19M2.2 5.5L17.8 14.5M2.2 14.5L17.8 5.5" stroke="var(--white)" stroke-width="2"/></svg></li>
      <li>Heating <svg width="18" height="18" viewBox="0 0 20 20" aria-hidden="true"><path d="M10 1C13 6 16 9 16 13a6 6 0 0 1-12 0c0-3 2-5 3-6 0 2 1 3 2 3 0-4 1-6 1-9Z" fill="var(--white)"/></svg></li>
      <li>Plumbing <svg width="18" height="18" viewBox="0 0 20 20" aria-hidden="true"><path d="M4 2V11a6 6 0 0 0 12 0V2" fill="none" stroke="var(--white)" stroke-width="3"/></svg></li>
    </ul>
    <p class="promise">Solutions<br>You Can<br>Trust</p>
  </section>

  <section class="panel panel-rear" aria-label="Trailer rear panel">
    <svg class="layer" width="360" height="360" viewBox="0 0 360 360">
      <path d="M120 0H360V300Q300 330 230 320Z" fill="var(--orange)"/>
      <circle cx="182" cy="170" r="158" fill="none" stroke="var(--blue)" stroke-width="26" stroke-dasharray="430 560" transform="rotate(100 182 170)"/>
      <circle cx="185" cy="165" r="140" fill="var(--orange)"/>
      <circle cx="192" cy="158" r="132" fill="var(--ink)"/>
    </svg>
    <div class="flag" style="left:0;top:0;width:230px;height:75px;opacity:.5" role="img" aria-label="Grayscale waving United States flag"></div>

    <p class="brand">PACH</p>
    <p class="phone">
      <svg width="18" height="18" viewBox="0 0 24 24" aria-hidden="true"><circle cx="12" cy="12" r="12" fill="var(--white)"/><path d="M8 6l2 3-1.5 1.5a8 8 0 0 0 5 5L15 14l3 2-1 2.5C11 18 6 13 5.5 7Z" fill="var(--ink)"/></svg>
      555-304-2617
    </p>
  </section>

</main>
</body>
</html>
```